8"x5" postcard for Wireless Internet introduction to new mountain town market

I need to market high speed internet to a resort mountain town without doing the obvious laptop on a mountain top thing, so tired. We are going to be competing directly with another provider with same cost, but we will be offering free installation. The area is Aspen Colorado, so the clientele are outdoor types who have suffered for years from being disconnected in their mountain town. We offer fast internet and excellent customer service from people who live in their neck of the woods.

Target Market(s)

23-55 years old, both resort living, families and ski bums

Font styles to use
Sans Serif

Colors

Designer to choose colors to be used in the design.

Requirements
Must have
• Visual appeal and fresh verbiage. We don't mind being a little edgy. We are a young company and we want to appeal to people looking for a provider who gets them. We prefer a clean look.
Nice to have
• Nice to have colors that match our logo
Should not have
• stuffy concepts or verbiage that is too much like a car salesman. We don't want to look like a 'big box' company.

```html
<!DOCTYPE html>
<html lang="en">
<head>
<meta charset="utf-8">
<title>Ridgeway Broadband Postcard</title>
<link href="https://fonts.googleapis.com/css2?family=Oswald:wght@600;700&family=Poppins:wght@400;500;600;700&display=swap" rel="stylesheet">
<style>
:root{
  --stage:#d9d9d9;
  --ink:#1f1f1f;
  --yellow:#ffd21a;
  --gold:#f6b40e;
  --orange:#ff8c00;
  --orange-deep:#f57c00;
  --paper:#ffffff;
  --paper-soft:#f1f1f1;
  --grey-text:#6b6b6b;
}
*{margin:0;padding:0;box-sizing:border-box}
html,body{width:1200px;height:1014px;overflow:hidden;background:var(--stage)}
body{position:relative;font-family:'Poppins',sans-serif;color:var(--ink)}
.card{position:absolute;top:97px;width:550px;height:879px;background:var(--paper);overflow:hidden}
.card--front{left:37px}
.card--back{left:614px}

/* FRONT */
.hero{position:absolute;left:0;top:0;width:550px;height:438px}
.hero__photo{position:absolute;inset:0;background:radial-gradient(ellipse at 75% 55%,#e9a21a 0%,#f1b526 30%,#f7cf3a 60%,#e9b026 100%)}
.headline{position:absolute;left:22px;font-family:'Oswald',sans-serif;font-weight:700;line-height:1;color:var(--ink);text-transform:uppercase;letter-spacing:.5px;white-space:nowrap}
.headline--1{top:26px;font-size:66px}
.headline--2{top:95px;font-size:50px}
.headline--3{top:196px;font-size:70px}
.headline--4{top:268px;font-size:46px}
.headline--5{top:362px;font-size:30px;font-weight:600}
.stripe-band{position:absolute;left:0;top:438px;width:550px;height:62px}
.front-body{position:absolute;left:0;top:500px;width:550px;height:303px;background:linear-gradient(#ffffff,#f3f3f3)}
.brand{position:absolute;display:flex;align-items:center}
.brand__dot{border-radius:50%;flex:none}
.brand__name{font-family:'Poppins',sans-serif;font-weight:700;line-height:1}
.front-body .brand{left:100px;top:30px}
.front-body .brand__dot{width:66px;height:66px;background:var(--gold);margin-right:16px}
.front-body .brand__name{font-size:36px;color:var(--ink)}
.features{position:absolute;left:24px;top:150px;list-style:none}
.features li{display:flex;align-items:center;height:30.5px;font-size:18px;white-space:nowrap}
.features svg{width:24px;height:24px;margin-right:13px;flex:none}
.features .caps{text-transform:uppercase}
.cta{position:absolute;right:0;top:154px;width:248px;height:67px}
.cta svg{position:absolute;inset:0}
.cta__text{position:absolute;right:20px;top:8px;text-align:right;font-weight:700;font-size:23px;line-height:1.15;color:var(--ink);white-space:nowrap}
.front-footer{position:absolute;left:0;top:803px;width:550px;height:76px;border-top:4px solid var(--gold);background:#f2f2f2;display:flex;align-items:center;justify-content:center;gap:28px}
.contact{display:flex;align-items:center;gap:12px;font-weight:600;font-size:19px;white-space:nowrap}
.contact__icon{width:30px;height:30px;border-radius:50%;display:flex;align-items:center;justify-content:center;flex:none}
.front-footer .contact__icon{background:var(--yellow)}

/* BACK */
.back-top{position:absolute;left:0;top:0;width:550px;height:435px;background:radial-gradient(ellipse at 50% 60%,#ffd21a 0%,#ffb30d 35%,#ff9200 70%,#f57c00 100%)}
.back-top .brand{left:112px;top:35px}
.back-top .brand__dot{width:62px;height:62px;background:var(--ink);margin-right:14px}
.back-top .brand__name{font-size:36px;color:var(--ink)}
.back-title{position:absolute;left:0;width:550px;text-align:center;font-family:'Oswald',sans-serif;font-weight:700;line-height:1;text-transform:uppercase;color:var(--ink);white-space:nowrap}
.back-title--1{top:150px;font-size:66px}
.back-title--2{top:224px;font-size:54px}
.back-copy{position:absolute;left:30px;width:490px;top:300px;text-align:center;font-size:17.5px;line-height:1.3;color:var(--ink)}
.back-contacts{position:absolute;left:0;width:550px;top:391px;display:flex;justify-content:center;gap:22px}
.back-contacts .contact{font-size:19px}
.back-contacts .contact__icon{width:28px;height:28px;background:var(--ink)}
.perforation{position:absolute;left:0;top:431px;width:550px;height:4px;background:repeating-linear-gradient(90deg,var(--ink) 0 14px,transparent 14px 21px)}
.stamp-box{position:absolute;left:444px;top:454px;width:76px;height:86px;border:2px solid var(--ink)}
</style>
</head>
<body>

<section class="card card--front">
  <div class="hero">
    <div class="hero__photo" role="img" aria-label="Photo of a cheetah standing in golden savanna grass"></div>
    <div class="headline headline--1">Want High Speed</div>
    <div class="headline headline--2">Internet?</div>
    <div class="headline headline--3">As Fast</div>
    <div class="headline headline--4">As Cheetah!</div>
    <div class="headline headline--5">Now at Aspen Colorado</div>
  </div>

  <svg class="stripe-band" viewBox="0 0 550 62" aria-hidden="true">
    <defs><linearGradient id="bandGold" x1="0" x2="1"><stop offset="0" stop-color="#f6b40e"/><stop offset="1" stop-color="#ffd21a"/></linearGradient></defs>
    <rect width="550" height="62" fill="#1f1f1f"/>
    <polygon points="262,0 286,0 228,62 204,62" fill="#eaeaea"/>
    <polygon points="458,0 550,0 550,62 400,62" fill="#eaeaea"/>
    <polygon points="478,0 550,0 550,62 420,62" fill="url(#bandGold)"/>
  </svg>

  <div class="front-body">
    <div class="brand">
      <span class="brand__dot"></span>
      <span class="brand__name">RIDGEWAY</span>
    </div>

    <ul class="features">
      <li><svg viewBox="0 0 24 24"><path d="M3 18a9 9 0 0 1 18 0" fill="none" stroke="#f6b40e" stroke-width="3"/><path d="M12 18l5-7" stroke="#1f1f1f" stroke-width="2"/></svg>50/100Mbps Speeds!</li>
      <li><svg viewBox="0 0 24 24"><circle cx="12" cy="9" r="5" fill="#f6b40e"/><path d="M4 23a8 6 0 0 1 16 0z" fill="#f6b40e"/><path d="M5 10a7 7 0 0 1 14 0" fill="none" stroke="#1f1f1f" stroke-width="1.6"/></svg>In-House Tech Support</li>
      <li class="caps"><svg viewBox="0 0 24 24"><path d="M4 4l16 16M20 4L4 20" stroke="#f6b40e" stroke-width="3.5" stroke-linecap="round"/></svg>Free Installation</li>
      <li><svg viewBox="0 0 24 24"><path d="M12 8v15M8 23h8" stroke="#f6b40e" stroke-width="2.5"/><circle cx="12" cy="6" r="2" fill="#f6b40e"/><path d="M7 2a6 6 0 0 0 0 8M17 2a6 6 0 0 1 0 8" fill="none" stroke="#f6b40e" stroke-width="1.6"/></svg>Rural-Broadband is our Speciality</li>
    </ul>

    <div class="cta">
      <svg viewBox="0 0 248 67" preserveAspectRatio="none" aria-hidden="true">
        <defs><linearGradient id="ctaGold" x1="0" x2="1"><stop offset="0" stop-color="#ffd21a"/><stop offset="1" stop-color="#f6b40e"/></linearGradient></defs>
        <polygon points="0,0 248,0 248,67 24,67" fill="url(#ctaGold)"/>
      </svg>
      <div class="cta__text">CALL US NOW<br>1.888.555.0147</div>
    </div>
  </div>

  <div class="front-footer">
    <div class="contact">
      <span class="contact__icon"><svg width="17" height="17" viewBox="0 0 24 24"><path d="M6 2l4 4-2 3c1 3 4 6 7 7l3-2 4 4-3 4C10 22 2 14 2 5z" fill="#1f1f1f"/></svg></span>
      1.888.555.0147
    </div>
    <div class="contact">
      <span class="contact__icon"><svg width="19" height="19" viewBox="0 0 24 24" fill="none" stroke="#1f1f1f" stroke-width="1.8"><circle cx="12" cy="12" r="10"/><ellipse cx="12" cy="12" rx="4.5" ry="10"/><path d="M2 12h20M4 6.5h16M4 17.5h16"/></svg></span>
      www.ridgewaynet.com
    </div>
  </div>
</section>

<section class="card card--back">
  <div class="back-top">
    <div class="brand">
      <span class="brand__dot"></span>
      <span class="brand__name">RIDGEWAY</span>
    </div>
    <div class="back-title back-title--1">Metro Services</div>
    <div class="back-title back-title--2">At Small Town Rate</div>
    <p class="back-copy">We offer first-class reliability and in-house Tech Support! Don't miss out join your business neighbors and get ready to thriled.</p>
    <div class="back-contacts">
      <div class="contact">
        <span class="contact__icon"><svg width="15" height="15" viewBox="0 0 24 24"><path d="M6 2l4 4-2 3c1 3 4 6 7 7l3-2 4 4-3 4C10 22 2 14 2 5z" fill="#ffd21a"/></svg></span>
        1.888.555.0147
      </div>
      <div class="contact">
        <span class="contact__icon"><svg width="17" height="17" viewBox="0 0 24 24" fill="none" stroke="#ffd21a" stroke-width="1.8"><circle cx="12" cy="12" r="10"/><ellipse cx="12" cy="12" rx="4.5" ry="10"/><path d="M2 12h20M4 6.5h16M4 17.5h16"/></svg></span>
        www.ridgewaynet.com
      </div>
    </div>
  </div>
  <div class="perforation"></div>
  <div class="stamp-box"></div>
</section>

</body>
</html>
```